Anzeigengestaltung für Autoglas-Unternehmen
Zielgruppe
Autoglas Felsbrunnen
Aufgabenstellung
Wir sorgen für klare Sicht!
Austausch von Frontscheiben – Heckscheiben und Seitenscheiben
Reparatur von Steinschlagschäden
Ihr zuverlässiger Partner in Sachen Sicherheit rund ums Autoglas!
unkompliziert – schnell – professionell
Auf Wunsch übernehmen wir für Sie die Abrechnung mit Ihrer Versicherung – schnell und unbürokratisch.
(soll hervorgehoben bzw. dicker geschrieben werden)
Wir verbauen ausschließlich original Scheiben der jeweiligen Autohersteller
( soll hervorgehoben bzw. dicker geschrieben werden)
Wir haben die Technik und das Know How
um eine fachgerechte Kalibrierung ihrer Assistenzsysteme wie z.B.
Spurhalteassistent, Abstandswarner, Notbremssystem etc. durchzuführen.

```html
<!DOCTYPE html>
<html lang="de">
<head>
<meta charset="utf-8">
<title>Autoglas Felsbrunnen – Anzeige</title>
<link rel="stylesheet" href="https://fonts.googleapis.com/css2?family=Roboto:wght@400;500;700;900&family=Roboto+Condensed:wght@300;700&display=swap">
<style>
  :root {
    --brand-red: #be1a2b;
    --ink: #000000;
    --paper: #ffffff;
    --photo-light: #d9d4d2;
    --photo-red: #b8323a;
    --photo-grey: #8f8c8c;
    --headline-veil: rgba(255, 255, 255, 0.72);
  }
  * { margin: 0; padding: 0; box-sizing: border-box; }
  html, body {
    width: 848px; height: 1200px; overflow: hidden;
    background: var(--paper);
  }
  .page { position: relative; width: 848px; height: 1200px; background: var(--paper); }
  .ad {
    position: absolute; left: 127px; top: 178px; width: 606px; height: 860px;
    background: var(--ink); overflow: hidden;
    font-family: "Roboto", Arial, sans-serif;
  }
  .url-band {
    position: absolute; left: 0; top: 0; width: 100%; height: 40px;
    background: var(--brand-red); color: var(--paper);
    font-family: "Roboto Condensed", Arial, sans-serif; font-weight: 700;
    font-size: 18px; line-height: 40px; text-align: center;
  }
  .hero {
    position: absolute; left: 0; top: 40px; width: 100%; height: 432px;
    background:
      radial-gradient(ellipse at 30% 35%, var(--photo-red) 0%, rgba(184,50,58,0.6) 30%, transparent 60%),
      radial-gradient(ellipse at 80% 60%, #a9a79a 0%, transparent 55%),
      linear-gradient(180deg, var(--photo-light) 0%, var(--photo-grey) 55%, var(--photo-light) 100%);
  }
  .headline {
    position: absolute; left: 0; width: 100%; text-align: center;
    color: var(--headline-veil); text-transform: uppercase;
    line-height: 1; white-space: nowrap;
  }
  .headline--intro { top: 13px; font-size: 52px; font-weight: 700; letter-spacing: -1px; }
  .headline--klare { top: 60px; font-size: 148px; font-weight: 900; letter-spacing: -2px; }
  .headline--sicht { top: 184px; font-size: 148px; font-weight: 900; letter-spacing: -2px; }
  .name-plate {
    position: absolute; z-index: 2; left: 57px; top: 381px; width: 489px; height: 106px;
    background: var(--paper);
    box-shadow: 0 3px 6px rgba(120,0,10,0.5);
    display: flex; align-items: center; justify-content: center;
    color: var(--ink); font-weight: 900; font-size: 42px; letter-spacing: -0.5px;
    white-space: nowrap;
  }
  .claim-band {
    position: absolute; z-index: 1; left: 0; top: 472px; width: 100%; height: 103px;
    background: var(--brand-red); color: var(--paper);
    font-family: "Roboto Condensed", Arial, sans-serif;
    padding: 24px 0 0 61px; font-size: 33px; line-height: 35px; font-weight: 300;
    white-space: nowrap;
  }
  .claim-band strong { font-weight: 700; }
  .services {
    position: absolute; left: 61px; top: 593px; width: 420px; list-style: none;
    color: var(--paper); font-family: "Roboto", Arial, sans-serif;
    font-weight: 500; font-size: 17.5px; line-height: 23px; text-transform: uppercase;
  }
  .services li { position: relative; padding-left: 18px; margin-bottom: 8px; }
  .services li::before {
    content: ""; position: absolute; left: 0; top: 4px;
    width: 13px; height: 13px; background: var(--brand-red);
  }
  .partner-badge {
    position: absolute; left: 490px; top: 596px; width: 56px; height: 36px;
    background: var(--paper); border: 3px solid var(--brand-red);
  }
  .copy {
    position: absolute; left: 61px; width: 485px; color: var(--paper);
    font-size: 14px; line-height: 17.3px; text-align: justify; hyphens: auto;
  }
  .copy--emphasis { top: 681px; font-family: "Roboto Condensed", Arial, sans-serif; font-weight: 700; font-size: 15px; }
  .copy--regular { top: 741px; font-weight: 400; }
  .footer {
    position: absolute; left: 61px; top: 808px; width: 485px; height: 36px;
    display: flex; align-items: center; color: var(--paper);
  }
  .footer__name { font-weight: 900; font-size: 14.5px; width: 172px; line-height: 16px; white-space: nowrap; }
  .footer__contact { font-size: 12.3px; line-height: 17px; white-space: nowrap; }
</style>
</head>
<body>
<div class="page">
  <article class="ad">
    <div class="url-band">www.autoglas-felsbrunnen.com</div>

    <section class="hero" role="img" aria-label="Foto einer Windschutzscheibe mit Steinschlag-Sprung, dahinter unscharf ein rotes Auto">
      <div class="headline headline--intro">Wir sorgen für</div>
      <div class="headline headline--klare">Klare</div>
      <div class="headline headline--sicht">Sicht</div>
    </section>

    <div class="name-plate">Autoglas Felsbrunnen</div>

    <div class="claim-band">
      Ihr <strong>zuverlässiger Partner</strong> in Sachen<br>
      <strong>Sicherheit rund ums Autoglas!</strong>
    </div>

    <ul class="services">
      <li>Austausch von: Frontscheiben,<br>Heckscheiben und Seitenscheiben</li>
      <li>Reparatur von Steinschlagschäden</li>
    </ul>
    <div class="partner-badge" aria-label="Partner-Emblem"></div>

    <p class="copy copy--emphasis">Auf Wunsch übernehmen wir für Sie die Abrechnung mit Ihrer Versicherung – schnell und unbürokratisch. Wir verbauen ausschließlich Originalscheiben der jeweiligen Autohersteller.</p>
    <p class="copy copy--regular">Wir haben die Technik und das Know-How um eine fachgerechte Kalibrierung ihrer Assistenzsysteme wie z.B.: Spurhalteassistent, Abstandswarner, Notbremssystem, etc. durchzuführen.</p>

    <footer class="footer">
      <div class="footer__name">Autoglas Felsbrunnen</div>
      <div class="footer__contact">
        Werkstr. 14 | 89599 Felsbrunnen | Tel.: 07391/4820573<br>
        info@autoglas-felsbrunnen.com
      </div>
    </footer>
  </article>
</div>
</body>
</html>
```